Re-Brand of TindelMox along with a new website design

TindelMox Ltd are a software & database development company using technologies such as PHP, C#, HTML, JQuery, Flex, AS3, MySQL, Oracle, MSSQL. We like to target all types of business from small to large.

We are great at coding but rubbish at design so thats where we need your help!

We want a complete re-brand of TindelMox including logo, website design, and business cards.

We would like a design that is clean but other than that, please feel free to be creative.

****Logo****
We are looking for a logo that appears professional but with a splash of colour that indicates a creative side. Please see below some logos that we like the look of:

We like this one because it has a nice simple and clear font for the name of the company but also an icon which is colourful and stands out. http://markvault.example/2013/03/brivelo/

We like this one because it is very clean, simple and again very clear. http://markvault.example/2013/03/quantorels/

http://markvault.example/2013/03/tide-lamp/
http://markvault.example/2013/02/velmorin/
http://markvault.example/2013/01/art-gallery-tarnwick/

As you will see from all of these examples, the font is very clear but there is always a graphic representing the company too. This is what we like.

****Website****
These are some of the examples of websites we like:
https://www.zestrune.example/
https://www.chatterlane.example/home
http://www.haldenimagery.example/
http://www.vistor.example/
http://quillbay.example/
https://www.usebriefnest.example/personal-intros
http://www.marmotpanel.example/

The current site can be found at tindelmox.example.uk

Reason: We have extended the deadline of the project by 5 days as I realise the original deadline was very tight.

Software

Requirements
Must have
• Website must have the following pages
Home
Services
Projects
About Us
Contact Us

```html
<!DOCTYPE html>
<html lang="en">
<head>
<meta charset="utf-8">
<title>TindelMox — Home</title>
<link rel="stylesheet" href="https://fonts.googleapis.com/css2?family=Questrial&display=swap">
<style>
  :root {
    --ink: #000000;
    --paper: #ffffff;
    --hero-deep: #0a1230;
    --hero-mid: #2a4a9a;
    --hero-light: #8fb0f0;
    --band-dark: #6f6f6f;
    --band-light: #dcdcdc;
    --rule: #cfcfcf;
    --font: "Questrial", "Century Gothic", sans-serif;
  }
  * { box-sizing: border-box; margin: 0; padding: 0; }
  html, body { width: 1200px; height: 789px; overflow: hidden; background: var(--ink); }
  body { font-family: var(--font); color: var(--paper); }
  .page { position: relative; width: 1200px; height: 789px; overflow: hidden; background: var(--ink); }

  /* Hero */
  .hero { position: absolute; left: 0; top: 0; width: 1200px; height: 277px; overflow: hidden; }
  .hero-visual {
    position: absolute; inset: 0;
    background:
      radial-gradient(ellipse 520px 200px at 640px 150px, rgba(143,176,240,.55), transparent 70%),
      linear-gradient(90deg, var(--hero-deep) 0%, var(--hero-mid) 45%, #5d7fd0 60%, var(--hero-deep) 100%);
  }
  .hero-topbar { position: absolute; left: 0; top: 0; width: 100%; height: 82px; background: rgba(0,0,0,.45); }
  .brand {
    position: absolute; top: 18px; left: 0; width: 100%; text-align: center;
    font-size: 44px; line-height: 1; letter-spacing: 1px; color: var(--paper);
  }
  .hero-title {
    position: absolute; top: 110px; left: 0; width: 100%; text-align: center;
    font-size: 88px; line-height: 1; font-weight: 400; color: var(--paper);
  }

  /* Navigation bands */
  .main-nav { position: absolute; left: 0; top: 277px; width: 1200px; height: 328px; list-style: none; }
  .nav-item { position: relative; height: 65.6px; }
  .nav-label {
    display: block; height: 26px; background: var(--ink); text-align: center;
    font-size: 19px; line-height: 24px; color: var(--paper); text-decoration: none;
  }
  .nav-band {
    height: 39.6px;
    background: linear-gradient(180deg, var(--band-dark) 0%, var(--band-light) 45%, #bdbdbd 70%, var(--band-dark) 100%);
    border-bottom: 1px solid #333;
  }
  .nav-chevron { position: absolute; left: 545px; top: 25px; width: 110px; height: 40px; }

  /* Footer */
  .site-footer { position: absolute; left: 0; top: 605px; width: 1200px; height: 184px; background: var(--ink); font-size: 16.5px; line-height: 20px; }
  .footer-links { position: absolute; left: 179px; top: 12px; list-style: none; }
  .footer-links li { height: 25.8px; }
  .footer-links a { color: var(--paper); text-decoration: none; }
  .footer-contact { position: absolute; left: 435px; top: 12px; font-style: normal; }
  .contact-name { margin-bottom: 20px; }
  .contact-row { display: flex; }
  .contact-key { width: 101px; }
  .footer-social { position: absolute; left: 834px; top: 36px; width: 203px; display: flex; justify-content: center; gap: 12px; font-size: 13px; }
  .footer-social a { color: var(--paper); text-decoration: none; }
  .footer-rule { position: absolute; left: 834px; top: 92px; width: 203px; border: 0; border-top: 1px solid var(--rule); }
  .footer-legal { position: absolute; left: 800px; top: 103px; width: 271px; text-align: center; font-size: 16px; line-height: 19.5px; }
</style>
</head>
<body>
<div class="page">
  <header class="hero">
    <div class="hero-visual" role="img" aria-label="Blue-lit photograph of a circuit board with an open hand reaching beneath it"></div>
    <div class="hero-topbar"></div>
    <div class="brand">tindelmox</div>
    <h1 class="hero-title">welcome to TindelMox</h1>
  </header>

  <ul class="main-nav">
    <li class="nav-item"><a class="nav-label" href="#">home</a><div class="nav-band"></div>
      <svg class="nav-chevron" viewBox="0 0 110 40"><polygon points="0,0 110,0 55,38" fill="#000"/><polyline points="2,2 55,38 108,2" fill="none" stroke="#fff" stroke-width="3"/></svg></li>
    <li class="nav-item"><a class="nav-label" href="#">services</a><div class="nav-band"></div>
      <svg class="nav-chevron" viewBox="0 0 110 40"><polygon points="0,0 110,0 55,38" fill="#000"/><polyline points="2,2 55,38 108,2" fill="none" stroke="#fff" stroke-width="3"/></svg></li>
    <li class="nav-item"><a class="nav-label" href="#">about us</a><div class="nav-band"></div>
      <svg class="nav-chevron" viewBox="0 0 110 40"><polygon points="0,0 110,0 55,38" fill="#000"/><polyline points="2,2 55,38 108,2" fill="none" stroke="#fff" stroke-width="3"/></svg></li>
    <li class="nav-item"><a class="nav-label" href="#">projects</a><div class="nav-band"></div>
      <svg class="nav-chevron" viewBox="0 0 110 40"><polygon points="0,0 110,0 55,38" fill="#000"/><polyline points="2,2 55,38 108,2" fill="none" stroke="#fff" stroke-width="3"/></svg></li>
    <li class="nav-item"><a class="nav-label" href="#">contact us</a><div class="nav-band"></div>
      <svg class="nav-chevron" viewBox="0 0 110 40"><polygon points="0,0 110,0 55,38" fill="#000"/><polyline points="2,2 55,38 108,2" fill="none" stroke="#fff" stroke-width="3"/></svg></li>
  </ul>

  <footer class="site-footer">
    <ul class="footer-links">
      <li><a href="#">home</a></li>
      <li><a href="#">services</a></li>
      <li><a href="#">projects</a></li>
      <li><a href="#">about us</a></li>
      <li><a href="#">contact us</a></li>
    </ul>
    <address class="footer-contact">
      <div class="contact-name">TindelMox</div>
      <div class="contact-row"><span class="contact-key">Telephone</span><span>01632 960 418</span></div>
      <div class="contact-row"><span class="contact-key">Email</span><span>contact@tindelmox.example.uk</span></div>
      <div class="contact-row"><span class="contact-key">Address</span><span>42 Harrowby Lane<br>Wexcombe<br>Northshire<br>WX4 7QB</span></div>
    </address>
    <nav class="footer-social">
      <a href="#">Friendloom</a>
      <a href="#">Chirpnet</a>
      <a href="#">Circlet</a>
    </nav>
    <hr class="footer-rule">
    <div class="footer-legal">
      <p>Copyright © 2013 TindelMox</p>
      <p>All Rights Reserved</p>
      <p>Terms of use</p>
    </div>
  </footer>
</div>
</body>
</html>
```